Buchcover-Design für Fachbuch
Tolle Entwürfe und ein sehr effiziente Zusammenarbeit. Können wir nur weiterempfehlen.
Zielgruppe
Unternehmensberatung im Thema Arbeitszeit. Wir haben ein Fachbuch zum Thema Arbeitszeit und Personaleinsatzplanung für Geschäftsführer, HR Mitarbeiter, Führungskräfte, Studenten und alle geschrieben, die sich o.g. Themen näher informieren möchten
Aufgabenstellung
Folgende Textelemente sollen zu sehen sein:
Autorennamen: Dr. Reinhold Kattner, Lothar Brenning
Titel: PLAN STARK Betrieb - Dienstzeiten und Schichtorganisation fair, rentabel und marktnah einrichten
Außerdem: Unter Mitwirkung von Prof. Anton K. Ruhland
Und: mit vielen Praxisbeispielen (ggf. als eine Art Plakette)
Auf der Rückseite soll ein Klappentext und 2 Zitate zu sehen sein:
Klappentext:
Die Welt verändert sich dramatisch. Digitalisierung, Fachkräftemangel, Wertewandel und nicht zuletzt Ausnahmezustände wie die Coronakrise stellen Unternehmen vor große Herausforderungen. Wie können Unternehmen flexibel und gleichzeitig wirtschaftlich, kunden- und mitarbeiterorientiert agieren?
Reinhold Kattner und Lothar Brenning sehen eine innovative Arbeitszeitgestaltung als entscheidenden Hebel an, um Unternehmen aller Branchen in schnelllebigen Märkten flexibel aufzustellen. Die Autoren beleuchten mit vielen Beispielen aus ihrer Beratungspraxis, warum Arbeitszeitsysteme dringend modernisiert werden müssen und welche Möglichkeiten Sie bereits heute haben, Arbeitszeit innovativ zu gestalten.
Sie erfahren alles Wissenswerte über klassische Modelle, wie z.B. Schichtplan, Gleitzeit, Vertrauensarbeitszeit, Zeitkontensystem und Teilzeit, über Workforce Management (Workforce Analytics, Personalbedarfsermittlung und Forecast, Personaleinsatzplanung, Zeiterfassung) bis hin zu Lebensarbeitszeit, Gruppenarbeit, Selbstorganisation, Homeoffice und New Work. Dabei lernen Sie nicht nur die Einzelkomponenten kennen, sondern erfahren auch, wie man diese geschickt zu einer für Mitarbeiter und Unternehmen gleichermaßen vorteilhaften Arbeitszeitsystematik kombiniert. Neben diesem strategischen Wissen vermitteln Ihnen die Autoren hilfreiche Methoden zur konkreten operativen Umsetzung dieser Themen.
Zitat 1:
„Durch die Weitergabe ihrer umfassenden Erfahrungen aus der Beratung ist es den Autoren in hervorragender Weise gelu..

```html
<!DOCTYPE html>
<html lang="de">
<head>
<meta charset="utf-8">
<title>Buchrückseite – PLAN STARK Betrieb</title>
<link href="https://fonts.googleapis.com/css2?family=Roboto:wght@400;700&display=swap" rel="stylesheet">
<style>
  :root {
    --green: #9cc33b;
    --green-light: #cfe0a0;
    --navy: #003a70;
    --navy-light: #7f8fb6;
    --ink: #0d3a78;
    --white: #ffffff;
  }
  html, body { margin: 0; padding: 0; overflow: hidden; }
  body {
    width: 848px; height: 1200px; background: var(--white);
    position: relative; font-family: "Roboto", Arial, sans-serif;
  }
  .back-cover {
    position: absolute; left: 81px; top: 190px; width: 686px; height: 889px;
    border: 1px solid #9aa3b5; box-sizing: border-box; background: var(--white);
  }
  .edge-strip { position: absolute; left: 0; top: 0; width: 16px; height: 100%; background: var(--navy); }
  .edge-strip::before { content: ""; position: absolute; left: 0; top: 0; width: 100%; height: 666px; background: var(--green); }
  .blurb {
    position: absolute; left: 36px; top: 12px; margin: 0;
    color: var(--ink); font-size: 15.1px; line-height: 21.4px; white-space: nowrap;
  }
  .blurb p { margin: 0 0 21.4px; }
  .isbn-label { position: absolute; left: 56px; top: 740px; color: var(--ink); font-size: 12.5px; }
  .isbn-box { position: absolute; left: 56px; top: 761px; width: 199px; height: 93px; border: 1px solid var(--navy); box-sizing: border-box; }
  .side { position: absolute; left: 428px; top: 0; width: 257px; height: 100%; }
  .side .stripe { position: absolute; left: 0; width: 8px; }
  .quote-panel { position: absolute; left: 0; width: 100%; box-sizing: border-box; padding: 0 12px 0 20px; color: var(--white); font-size: 13.7px; line-height: 19.9px; white-space: nowrap; }
  .quote-panel p { margin: 0 0 19.9px; }
  .quote-panel strong { font-weight: 700; }
  .quote-green { top: 0; height: 354px; background: var(--green); padding-top: 14px; }
  .quote-navy { top: 556px; height: 333px; background: var(--navy); padding-top: 28px; }
  .stripe-green { top: 0; height: 354px; background: var(--green-light); }
  .stripe-navy { top: 556px; height: 333px; background: var(--navy-light); }
  .warehouse-photo {
    position: absolute; left: 0; top: 354px; width: 100%; height: 202px;
    background: linear-gradient(135deg, #d9cfc0 0%, #c9b79a 40%, #e2dccf 70%, #b8a88c 100%);
  }
</style>
</head>
<body>
  <section class="back-cover">
    <div class="edge-strip"></div>

    <div class="blurb">
      <p>Die Welt verändert sich dramatisch. Digitalisierung,<br>Fachkräftemangel, Wertewandel und nicht zuletzt<br>Ausnahmezustände wie die Coronakrise stellen Unter-<br>nehmen vor große Herausforderungen. Wie können<br>Unternehmen flexibel und gleichzeitig wirtschaftlich,<br>kunden- und mitarbeiterorientiert agieren?</p>
      <p>Reinhold Kattner und Lothar Brenning sehen eine inno-<br>vative Arbeitszeitgestaltung als entscheidenden Hebel<br>an, um Unternehmen aller Branchen in schnelllebigen<br>Märkten flexibel aufzustellen. Die Autoren beleuchten<br>mit vielen Beispielen aus ihrer Beratungspraxis, war-<br>um Arbeitszeitsysteme dringend modernisiert werden<br>müssen und welche Möglichkeiten Sie bereits heute<br>haben, Arbeitszeit innovativ zu gestalten.</p>
      <p>Sie erfahren alles Wissenswerte über klassische<br>Modelle, wie z.B. Schichtplan, Gleitzeit, Vertrauens-<br>arbeitszeit, Zeitkontensystem und Teilzeit, über<br>Workforce Management (Workforce Analytics, Perso-<br>nalbedarfs-ermittlung und Forecast, Personaleinsatz-<br>planung, Zeiterfassung) bis hin zu Lebensarbeitszeit,<br>Gruppenarbeit, Selbstorganisation, Homeoffice und<br>New Work. Dabei lernen Sie nicht nur die Einzelkompo-<br>nenten kennen, sondern erfahren auch, wie man diese<br>geschickt zu einer für Mitarbeiter und Unternehmen<br>gleichermaßen vorteilhaften Arbeitszeitsystematik<br>kombiniert. Neben diesem strategischen Wissen ver-<br>mitteln Ihnen die Autoren hilfreiche Methoden zur<br>konkreten operativen Umsetzung dieser Themen.</p>
    </div>

    <div class="isbn-label">ISBN-Nr.:</div>
    <div class="isbn-box"></div>

    <aside class="side">
      <div class="quote-panel quote-green">
        <p>„Durch die Weitergabe ihrer<br>umfassenden Erfahrungen aus der<br>Beratung ist es den Autoren<br>in hervorragender Weise gelungen,<br>neue Einsichten und vertieftes<br>Expertenwissen sowohl zur Im-<br>plementierung von Workforce<br>Management-Lösungen als auch<br>zu konkreten Vorgehensweisen bei<br>der Personaleinsatzplanung zu<br>vermitteln.“</p>
        <p><strong>Anton K. Ruhland,</strong><br>Professor für Personalmanage-<br>ment an der HSTW Lindenau</p>
      </div>
      <div class="stripe stripe-green"></div>

      <div class="warehouse-photo" role="img" aria-label="Foto: Lagermitarbeiter mit Schutzhelm und Warnweste zwischen Regalen"></div>

      <div class="quote-panel quote-navy">
        <p>„Das vorliegende Buch von<br>Kattner und Brenning liefert den<br>entscheidenden Baustein zur<br>Humanisierung von Ökonomie<br>und Unternehmensorganisation<br>und hat das Potenzial zu dem<br>Standardwerk im Thema moderne<br>Arbeitszeitgestaltung und Work-<br>force Management zu werden.“</p>
        <p><strong>Dr. Matthias Krellner,</strong> Initiator des<br>Kompetenznetzwerks<br>Fachforum Werkraum &amp; Top 3 HR In-<br>fluencer 2020 (Arbeitswelt Journal)</p>
      </div>
      <div class="stripe stripe-navy"></div>
    </aside>
  </section>
</body>
</html>
```